self-employed education content specialist/consultant needs business card and logo design

I need a design for a double-sided business card (and logo) for my nascent consultancy business based in London UK, to hand out at a London trade show in a couple of weeks. The business simply has my name, "Marcus Tenwold".

I describe my service as a "content and engagement consultant". In essence I cover 2 areas:
- Advice to organisations on effective strategies and tactics for creating and distributing large volumes of media-rich content (video and interactive) for learning, training and professional development, that successfully engages and impacts on students and their teachers.
- Advice on growing and maintaining customer/end-user engagement to help maximise the reach and usage of this content.

I have uploaded a weighted list of key words that offer I hope a good feel of "the brand".

In terms of design I have put together a very rough initial idea for the card (see attached doc), which gives an idea of the key messages in text, but I feel it is not working visually, and looks too amateur. In particular I think the background/visuals of the info side needs work; the word cloud on the back of the card is perhaps rather "passé" and could be improved on; there is no "logo" at present; and I think overall it's not very "creative", i.e. it doesn't "stand out".

I am not set on font or background colours/design. The font itself should not be too businessy or too "comic sans", hence I've currently gone for something like Odile or Playfair Display.

Also note that
1. given budget and time constraints, I'm looking for designs for printing on paper, and to be of a fairly standard business card shape/size.
2. I have no web address at present, but will need a card design that can cope with this being added at a later date.

Overall I am hoping for something fairly clean, simple and clear, that will impress and speak to senior managers/business owners working in the education and edtech sectors.

As a self-employed consultant my budget is limited, so I don't expect the world for what I can offer, but am hoping that there are design experts out there who can swiftly interpret my brief and produce something suitable for my needs.

Target Market(s)

senior managers/business owners working in the education and edtech sectors.

Contact Information for Business Card

marcus tenwold
content and engagement consultant
education - training - development
+44 (0) 7731 482905
marcus.tenwold@quorvane.com

Font styles to use
Other font styles liked:
• Odile or Playfair Display are my favourites for now.

Colors

Designer to choose colors to be used in the design.

```html
<!DOCTYPE html>
<html lang="en">
<head>
<meta charset="utf-8">
<title>Marcus Tenwold — Business Card</title>
<link rel="stylesheet" href="https://fonts.googleapis.com/css2?family=Playfair+Display:wght@400;600&display=swap">
<style>
  :root {
    --ink-dark: #333333;
    --brand-blue: #36658f;
    --paper: #ffffff;
    --text-light: #f2f4f7;
    --serif: "Playfair Display", Georgia, serif;
  }
  * { margin: 0; padding: 0; box-sizing: border-box; }
  html, body {
    width: 1200px; height: 900px; overflow: hidden;
    background: var(--paper);
    font-family: var(--serif);
    font-variant-numeric: lining-nums;
  }
  .card {
    position: absolute;
    left: 285px;
    width: 630px; height: 359px;
    border-radius: 18px;
    overflow: hidden;
    background: var(--ink-dark);
  }
  .card--front { top: 66px; }
  .card--back { top: 471px; }
  .card__art { position: absolute; inset: 0; width: 100%; height: 100%; }

  /* Keyword cloud */
  .keyword-cloud {
    position: absolute;
    left: 0; right: 0; top: 27px;
    color: var(--text-light);
    text-transform: uppercase;
    line-height: 21.6px;
  }
  .keyword-cloud__line { display: flex; justify-content: center; align-items: baseline; gap: 6px; height: 21.6px; }
  .kw-sm { font-size: 11.5px; }
  .kw-md { font-size: 14.5px; }
  .kw-lg { font-size: 17px; }
  .kw-xl { font-size: 20px; }

  /* Name mark */
  .name-mark {
    position: absolute;
    right: 40px; top: 52px;
    color: var(--brand-blue);
    font-size: 27px; font-weight: 400;
    line-height: 32px;
    letter-spacing: 0.5px;
    text-transform: uppercase;
    text-align: right;
  }

  /* Identity block */
  .identity {
    position: absolute;
    left: 45px; top: 232px;
    color: var(--text-light);
  }
  .identity__name {
    font-size: 22px; font-weight: 600;
    letter-spacing: 1px;
    text-transform: uppercase;
    margin-bottom: 5px;
    line-height: 30px;
  }
  .identity__line { font-size: 15px; line-height: 20px; letter-spacing: 0.2px; }

  .contact {
    position: absolute;
    left: 378px; top: 274px;
    color: var(--text-light);
    font-size: 14.5px;
    list-style: none;
  }
  .contact__item { display: flex; align-items: center; gap: 12px; height: 26px; white-space: nowrap; }
  .contact__icon { width: 17px; height: 17px; fill: var(--text-light); flex: none; }
</style>
</head>
<body>

<section class="card card--front" aria-label="Card front">
  <svg class="card__art" viewBox="0 0 630 359" aria-hidden="true">
    <path fill="var(--brand-blue)" d="M215,0 L630,0 L630,72 C575,215 505,315 420,359 L0,359 L0,284 C48,168 120,62 215,0 Z"/>
  </svg>
  <div class="keyword-cloud">
    <div class="keyword-cloud__line"><span class="kw-md">Reach</span></div>
    <div class="keyword-cloud__line"><span class="kw-sm">Strategy</span><span class="kw-lg">Media</span><span class="kw-sm">Growth</span></div>
    <div class="keyword-cloud__line"><span class="kw-xl">Engagement</span><span class="kw-xl">Content</span></div>
    <div class="keyword-cloud__line"><span class="kw-xl">Learning</span><span class="kw-sm">Usage</span><span class="kw-xl">Students</span></div>
    <div class="keyword-cloud__line"><span class="kw-lg">Teachers</span><span class="kw-md">Distribution</span><span class="kw-xl">Video</span></div>
    <div class="keyword-cloud__line"><span class="kw-md">End-User</span><span class="kw-xl">Consultancy</span><span class="kw-md">Tactics</span></div>
    <div class="keyword-cloud__line"><span class="kw-xl">Interactive</span><span class="kw-sm">Schools Impact Ideas</span></div>
    <div class="keyword-cloud__line"><span class="kw-md">Organisations</span><span class="kw-xl">Training</span><span class="kw-md">Edtech</span></div>
    <div class="keyword-cloud__line"><span class="kw-xl">Education</span><span class="kw-sm">Customers</span><span class="kw-xl">Creative</span></div>
    <div class="keyword-cloud__line"><span class="kw-xl">Media-Rich Production</span></div>
    <div class="keyword-cloud__line"><span class="kw-sm">Online Audience</span><span class="kw-lg">Development</span></div>
    <div class="keyword-cloud__line"><span class="kw-xl">Partnership</span><span class="kw-sm">Digital Skills</span></div>
    <div class="keyword-cloud__line"><span class="kw-sm">Advice</span><span class="kw-lg">Platforms</span><span class="kw-md">Scale</span></div>
    <div class="keyword-cloud__line"><span class="kw-md">London</span></div>
  </div>
</section>

<section class="card card--back" aria-label="Card back">
  <svg class="card__art" viewBox="0 0 630 359" aria-hidden="true">
    <path fill="var(--brand-blue)" d="M0,197 C40,184 80,178 120,178 C250,178 340,240 470,240 C540,240 590,218 630,200 L630,359 L0,359 Z"/>
    <path fill="var(--brand-blue)" d="M340,184 C420,214 540,214 630,186 L630,199 C545,232 420,226 340,184 Z"/>
  </svg>

  <div class="name-mark">Marcus<br>Tenwold</div>

  <div class="identity">
    <h1 class="identity__name">Marcus Tenwold</h1>
    <p class="identity__line">Content and Engagement Consultant</p>
    <p class="identity__line">Education – Training – Development</p>
    <p class="identity__line">Video - Online - Interactive</p>
  </div>

  <ul class="contact">
    <li class="contact__item">
      <svg class="contact__icon" viewBox="0 0 24 24" aria-hidden="true"><path d="M6.6 10.8c1.4 2.8 3.8 5.1 6.6 6.6l2.2-2.2c.3-.3.7-.4 1-.2 1.1.4 2.3.6 3.6.6.6 0 1 .4 1 1V20c0 .6-.4 1-1 1C10.6 21 3 13.4 3 4c0-.6.4-1 1-1h3.5c.6 0 1 .4 1 1 0 1.3.2 2.5.6 3.6.1.3 0 .7-.2 1L6.6 10.8z"/></svg>
      <span>+44 (0) 7731 482905</span>
    </li>
    <li class="contact__item">
      <svg class="contact__icon" viewBox="0 0 24 24" aria-hidden="true"><path d="M2 5h20v2.2l-10 6.3L2 7.2z M2 9.6l10 6.3 10-6.3V19H2z"/></svg>
      <span>marcus.tenwold@quorvane.com</span>
    </li>
  </ul>
</section>

</body>
</html>
```